Brookvale Renovations - Get the creative juices going!!

Brookvale does not do the actual renovation work. The company provides high end project management of renovation (primarily residential - with an eye toward commercial) The renovation work could look very different between projects. This company manages the work of contractors, architects and interior designers (either subcontracted directly by Brookvale or hired by the client and entrusted to Brookvale to manage). Clients are high end in the economic scale and the card needs to have a high end feel to it.

The owner is female, but the audience will be heavily slanted male. It should not be a "feminine" or "masculine" looking card. If anything, slant more on the masculine side. Clean, simple, yet creative and artistically appealing. The card design should complement and in no way compete with the logo.

When people think of our company: trust, integrity, dynamic, limitless possibilities, transition, energy, creative. We plan to expand in the future to be international.

There will also be a contest running for stationary. Please check that section, as well.

***Black is 80-90 percent black. Not stark black

Tight timeline. Needs cards printed quickly!

```html
<!DOCTYPE html>
<html lang="en">
<head>
<meta charset="utf-8">
<title>Brookvale Renovations – Business Card</title>
<link href="https://fonts.googleapis.com/css2?family=Lato:ital,wght@0,300;0,400;0,700;1,400&display=swap" rel="stylesheet">
<style>
  :root {
    --backdrop: #6a6a6a;
    --card-charcoal: #434343;
    --teal: #14a89c;
    --white: #ffffff;
    --soft-white: #ececec;
  }
  html, body {
    margin: 0;
    width: 1200px;
    height: 900px;
    overflow: hidden;
    background: var(--backdrop);
    font-family: "Lato", sans-serif;
  }
  .card {
    position: absolute;
    left: 75px;
    top: 150px;
    width: 1050px;
    height: 600px;
    background: var(--card-charcoal);
    overflow: hidden;
    box-shadow: 0 14px 40px rgba(0, 0, 0, 0.35);
  }
  .brand {
    position: absolute;
    left: 64px;
    top: 112px;
    display: flex;
    align-items: center;
    gap: 14px;
  }
  .brand-square {
    width: 18px;
    height: 18px;
    background: var(--white);
  }
  .brand-name {
    margin: 0;
    font-size: 30px;
    font-weight: 400;
    letter-spacing: 1px;
    color: var(--white);
    text-transform: uppercase;
  }
  .holder-name {
    position: absolute;
    left: 64px;
    top: 175px;
    margin: 0;
    font-size: 54px;
    font-weight: 300;
    letter-spacing: 1px;
    color: var(--white);
  }
  .holder-title {
    position: absolute;
    left: 66px;
    top: 244px;
    margin: 0;
    font-size: 27px;
    font-weight: 700;
    color: var(--teal);
  }
  .contact-list {
    position: absolute;
    left: 66px;
    top: 298px;
    margin: 0;
    padding: 0;
    list-style: none;
    font-size: 26px;
    line-height: 38px;
    color: var(--soft-white);
  }
  .contact-label { font-style: italic; }
  .wave {
    position: absolute;
    left: 0;
    bottom: 0;
    width: 1050px;
    height: 260px;
  }
  .wave-highlight { fill: var(--soft-white); }
  .wave-band { fill: var(--teal); }
  .street-address {
    position: absolute;
    left: 66px;
    bottom: 38px;
    margin: 0;
    font-size: 27px;
    font-weight: 700;
    color: var(--white);
  }
</style>
</head>
<body>
  <div class="card">
    <div class="brand">
      <span class="brand-square"></span>
      <p class="brand-name">Brookvale Renovations</p>
    </div>

    <h1 class="holder-name">YOUR NAME</h1>
    <p class="holder-title">Title text</p>

    <ul class="contact-list">
      <li><span class="contact-label">phone:</span> 123-456-7890</li>
      <li><span class="contact-label">web:</span> yourdomain.com</li>
      <li><span class="contact-label">email:</span> yourname@yourdomain.com</li>
    </ul>

    <svg class="wave" viewBox="0 0 1050 260" preserveAspectRatio="none" aria-hidden="true">
      <path class="wave-highlight" d="M0 112 C 300 100, 600 74, 800 64 C 920 58, 990 46, 1050 30 L1050 260 L0 260 Z"/>
      <path class="wave-band" d="M0 142 C 300 124, 600 96, 800 84 C 920 78, 990 64, 1050 50 L1050 260 L0 260 Z"/>
    </svg>

    <p class="street-address">Street address goes here, Suite #303, Alt Bldg, NY 82365</p>
  </div>
</body>
</html>
```